Fern Guildworks Business Cards

Looking or a business card design for my start-up, called "Fern Guildworks".
Our tagline is "Unleashing the human potential for good through leadership, culture, and education."
Our mission-driven work includes professional/personal development workshops, educational design services, organizational & project management consulting, and coaching services for K-12 schools, organizations, and individuals.
You can check out the website we're building at fernguildworks.com
I select projects from designers who are highly responsive to feedback, engage in dialog about revisions, and provide all root/source documents (so please state in your initial submission that you agree to do so).
Looking forward to seeing your great designs!!
Updates
Hello everyone,
Industry/Entity Type
Building
Requirements
Must have
- Looking for a two sided design that includes our logo (I am uploading two variations that I would like incorporated in .ai format) and website on both sides.
The front side must include:
Logo, Name, Title, Phone, Email, Twitter handle
The back side must include: Logo, @ferngild (our organizational twitter handle)
Nice to have
- I like the rounded corner business cards, but that is not absolutely essential.
Should not have
- Colors beyond those presented in our logo.

```html
<!DOCTYPE html>
<html lang="en">
<head>
<meta charset="utf-8">
<title>Fern Guildworks Business Cards</title>
<link href="https://fonts.googleapis.com/css2?family=Tinos:wght@400;700&display=swap" rel="stylesheet">
<style>
  :root {
    --stone: #a39a91;
    --stone-dark: #8f867d;
    --sky: #6ccbe0;
    --paper: #ffffff;
    --backdrop: #e6e6e6;
  }
  * { box-sizing: border-box; margin: 0; padding: 0; }
  html, body {
    width: 1200px; height: 901px; overflow: hidden;
    background: var(--backdrop);
    font-family: "Tinos", "Times New Roman", serif;
    color: var(--stone);
  }
  .sheet {
    position: relative; width: 1200px; height: 901px;
    display: flex; align-items: center; justify-content: center; gap: 60px;
  }
  .card {
    position: relative; width: 525px; height: 300px;
    background: var(--paper);
    border-radius: 10px;
    box-shadow: 0 6px 18px rgba(0,0,0,0.12);
    overflow: hidden;
  }
  /* Back side */
  .card--back {
    display: flex; flex-direction: column; align-items: center; justify-content: center;
  }
  .brand { display: flex; align-items: center; gap: 12px; }
  .brand__dot { width: 26px; height: 26px; border-radius: 50%; background: var(--sky); flex: none; }
  .brand__name {
    font-size: 34px; letter-spacing: 1px; text-transform: uppercase; color: var(--stone);
  }
  .tagline {
    margin-top: 6px; font-size: 11px; letter-spacing: 5px; text-transform: uppercase; color: var(--stone);
  }
  .card--back .website {
    position: absolute; bottom: 26px; left: 0; right: 0; text-align: center;
    font-size: 13px; color: var(--stone-dark);
  }
  /* Front side */
  .card--front .identity {
    position: absolute; left: 26px; top: 118px; width: 240px;
    display: flex; flex-direction: column; align-items: center;
  }
  .card--front .brand__name { font-size: 20px; }
  .card--front .brand__dot { width: 18px; height: 18px; }
  .card--front .tagline { font-size: 7px; letter-spacing: 3px; }
  .divider {
    position: absolute; left: 288px; top: 36px; width: 1px; height: 168px; background: var(--sky);
  }
  .person { position: absolute; right: 42px; top: 34px; text-align: right; }
  .person__name { font-size: 19px; text-transform: uppercase; color: var(--stone); }
  .person__title { font-size: 14px; text-transform: uppercase; color: var(--sky); letter-spacing: 0.5px; }
  .tab {
    position: absolute; right: 0; top: 46px; width: 12px; height: 28px; background: var(--sky);
  }
  .contacts {
    position: absolute; right: 22px; top: 158px; list-style: none; text-align: right;
    font-size: 13.5px; line-height: 19px; color: var(--stone-dark);
  }
  .contacts li { display: flex; align-items: center; justify-content: flex-end; gap: 10px; }
  .contacts svg { width: 10px; height: 10px; flex: none; }
  .contacts .strong { font-weight: 700; }
  .baseline {
    position: absolute; left: 0; right: 0; bottom: 24px; height: 2px; background: var(--sky);
  }
</style>
</head>
<body>
<main class="sheet">
  <section class="card card--back" aria-label="Business card back">
    <div class="brand">
      <span class="brand__dot"></span>
      <span class="brand__name">Fern Guildworks</span>
    </div>
    <p class="tagline">Leadership | Culture | Education</p>
    <p class="website">www.fernguildworks.com</p>
  </section>

  <section class="card card--front" aria-label="Business card front">
    <div class="identity">
      <div class="brand">
        <span class="brand__dot"></span>
        <span class="brand__name">Fern Guildworks</span>
      </div>
      <p class="tagline">Leadership | Culture | Education</p>
    </div>
    <span class="divider"></span>
    <div class="person">
      <p class="person__name">Maren Oakley</p>
      <p class="person__title">President</p>
    </div>
    <span class="tab"></span>
    <ul class="contacts">
      <li>+ 0 123 456 789
        <svg viewBox="0 0 10 10"><rect x="2.5" y="0.5" width="5" height="9" rx="1" fill="none" stroke="var(--sky)"/></svg></li>
      <li>maren@fernguildworks.com
        <svg viewBox="0 0 10 10"><rect x="0.5" y="2" width="9" height="6" fill="none" stroke="var(--sky)"/><path d="M0.5 2 L5 5.5 L9.5 2" fill="none" stroke="var(--sky)"/></svg></li>
      <li>@ferngild
        <svg viewBox="0 0 10 10"><circle cx="5" cy="5" r="4" fill="var(--sky)"/></svg></li>
      <li><span>www.<span class="strong">fernguildworks</span>.com</span>
        <svg viewBox="0 0 10 10"><circle cx="5" cy="5" r="4" fill="none" stroke="var(--sky)"/><path d="M1 5 H9 M5 1 C3 3.5 3 6.5 5 9 M5 1 C7 3.5 7 6.5 5 9" fill="none" stroke="var(--sky)" stroke-width="0.7"/></svg></li>
    </ul>
    <span class="baseline"></span>
  </section>
</main>
</body>
</html>
```